Software Development Consulting Company Needs Business Card Design

We need a new business card design for our consultants at Marendo Solutions (marendosolutions.example). We are a small firm that provides high-end software development and methodology consulting to medium to large enterprise IT organizations.

Our logo uses Futura for the font and we would like to stick with navy blue and canary yellow for the logo colors. Attached are normal and reversed versions of our logos in illustrator format.
Updates

Hi Everyone, Thank yo very much for your amazing design ideas. I have created a poll for this project and our employees will be voting on the design they wish to use. We will be making a decision this Wednesday (October 22nd). Thanks again, Gavin Hartwell

Industry/Entity Type

Business

```html
<!DOCTYPE html>
<html lang="en">
<head>
<meta charset="utf-8">
<title>Marendo Solutions — Business Card</title>
<link rel="stylesheet" href="https://fonts.googleapis.com/css2?family=Jost:wght@400;500&display=swap">
<style>
  :root {
    --navy: #142d56;
    --canary: #f7e51a;
    --paper: #ffffff;
    --backdrop: #e9e6e1;
  }
  * { box-sizing: border-box; margin: 0; padding: 0; }
  html, body {
    width: 1200px; height: 900px; overflow: hidden;
    background: var(--backdrop);
    font-family: "Jost", "Futura", sans-serif;
  }
  .sheet {
    width: 1200px; height: 900px;
    display: flex; flex-direction: column; align-items: center; justify-content: center;
    gap: 40px;
  }
  .card {
    position: relative;
    width: 700px; height: 400px;
    box-shadow: 0 6px 18px rgba(0,0,0,0.18);
    overflow: hidden;
  }
  .card--front {
    background: var(--navy);
    display: flex; align-items: center; justify-content: center;
  }
  .card--back { background: var(--paper); }

  .company-name {
    font-weight: 500; font-size: 40px; line-height: 1; letter-spacing: 0;
    white-space: nowrap;
  }
  .card--front .company-name { color: var(--paper); }
  .card--back .company-name {
    position: absolute; top: 48px; left: 44px;
    color: var(--navy);
  }

  .person {
    position: absolute; top: 140px; right: 44px; text-align: right; color: var(--navy);
  }
  .person__name { font-weight: 500; font-size: 22px; letter-spacing: 0.04em; line-height: 1.2; }
  .person__title { font-weight: 400; font-size: 14px; letter-spacing: 0.08em; line-height: 1.4; }

  .rule {
    position: absolute; top: 212px; left: 44px; right: 0;
    height: 2px; background: var(--canary);
  }

  .contact {
    position: absolute; right: 44px; top: 236px;
    list-style: none; color: var(--navy);
  }
  .contact__item {
    display: flex; align-items: center; justify-content: flex-end; gap: 10px;
    font-size: 15px; font-weight: 400; line-height: 32px; white-space: nowrap;
  }
  .contact__icon {
    width: 18px; height: 18px; border-radius: 50%;
    background: var(--navy); display: flex; align-items: center; justify-content: center;
    flex: none;
  }
  .contact__icon svg { width: 10px; height: 10px; }
  .icon-fill { fill: var(--canary); }
  .icon-line { fill: none; stroke: var(--canary); stroke-width: 1.2; stroke-linejoin: round; }
</style>
</head>
<body>
<main class="sheet">

  <section class="card card--front" aria-label="Card front">
    <p class="company-name">Marendo Solutions</p>
  </section>

  <section class="card card--back" aria-label="Card back">
    <p class="company-name">Marendo Solutions</p>

    <div class="person">
      <p class="person__name">GAVIN HARTWELL</p>
      <p class="person__title">PRINCIPAL CONSULTANT</p>
    </div>

    <div class="rule"></div>

    <ul class="contact">
      <li class="contact__item">555-014-2290
        <span class="contact__icon"><svg viewBox="0 0 10 10"><path class="icon-fill" d="M2 1l2 2-1 1c.6 1.3 1.7 2.4 3 3l1-1 2 2-1.5 1.5C4 9 1 6 .5 2.5z"/></svg></span>
      </li>
      <li class="contact__item">gavin.hartwell@marendosolutions.example
        <span class="contact__icon"><svg viewBox="0 0 10 10"><path class="icon-line" d="M1.5 2.5h7v5h-7z M1.5 2.5l3.5 3 3.5-3"/></svg></span>
      </li>
      <li class="contact__item">2450 Lakeview Commons Dr, Fairmont, MO 63000
        <span class="contact__icon"><svg viewBox="0 0 10 10"><path class="icon-fill" d="M5 1l4 4H8v4H6V6H4v3H2V5H1z"/></svg></span>
      </li>
    </ul>
  </section>

</main>
</body>
</html>
```